Billboard design - consider what a billboard is

Design a billboard using my logo - Billboard is 6m x 3m
A Billboard is advertising for my company that is on a big sign.

Has to be clean and easy to read, and ideally highlights that we are Residential and Commercial builders.

Keep it clean and easy to read

The contact number for the board is

022 583 7092
www.harbourframeworks.co.nz
info@harbourframeworks.co.nz

Doesnt have to have all contact details if it doesnt fit

Has to catch peoples attention to contact us if they need a builder

Can you please change the sign to be all white writing, with black background ?
Updates

Please consider what a billboard is...

The design needs to be suitable for a billboard..

Target Market(s)

people driving past

Industry/Entity Type

Construction

Logo Text

Wellington Builder, website email address, contact number

Colors
0054AA
0677BA
7BADD7
CADEEF
E8F1F8

Requirements
Must have
• Easy to read
Nice to have
• easy to read, can clearly see contact details

```html
<!DOCTYPE html>
<html lang="en">
<head>
<meta charset="utf-8">
<title>Harbour Frameworks – Billboard 6m x 3m</title>
<link href="https://fonts.googleapis.com/css2?family=Barlow:wght@600;800&family=Inter:wght@400&display=swap" rel="stylesheet">
<style>
  :root {
    --page: #fdfdfd;
    --board: #000000;
    --brand-blue: #588bc9;
    --steel-grey: #929497;
    --white: #ffffff;
    --label-ink: #111111;
  }
  * { margin: 0; padding: 0; box-sizing: border-box; }
  html, body {
    width: 1200px;
    height: 1000px;
    overflow: hidden;
    background: var(--page);
  }
  .canvas {
    position: relative;
    width: 1200px;
    height: 1000px;
  }
  .size-label {
    position: absolute;
    left: 194px;
    top: 232px;
    font-family: "Inter", sans-serif;
    font-weight: 400;
    font-size: 38px;
    color: var(--label-ink);
  }
  .billboard {
    position: absolute;
    left: 189px;
    top: 294px;
    width: 822px;
    height: 412px;
    background: var(--board);
    box-shadow: 7px 7px 7px rgba(0, 0, 0, 0.45);
    overflow: hidden;
    font-family: "Barlow", sans-serif;
  }
  .brand-name {
    position: absolute;
    left: 62px;
    top: 108px;
    color: var(--brand-blue);
    font-weight: 800;
    text-transform: uppercase;
    line-height: 0.95;
  }
  .brand-name .line-main { display: block; font-size: 90px; letter-spacing: 1px; }
  .brand-name .line-sub { display: block; font-size: 56px; letter-spacing: 1px; }
  .divider {
    position: absolute;
    left: 490px;
    top: 137px;
    width: 1.5px;
    height: 83px;
    background: var(--white);
  }
  .tagline {
    position: absolute;
    left: 509px;
    top: 136px;
    color: var(--steel-grey);
    font-weight: 600;
    font-size: 25px;
    line-height: 31px;
    text-transform: uppercase;
  }
  .contact-band {
    position: absolute;
    left: 0;
    top: 0;
    width: 822px;
    height: 412px;
  }
  .phone-icon {
    position: absolute;
    left: 56px;
    top: 337px;
    width: 42px;
    height: 42px;
  }
  .phone-number {
    position: absolute;
    left: 111px;
    top: 320px;
    color: var(--white);
    font-weight: 800;
    font-size: 62px;
    line-height: 71px;
    letter-spacing: 0.5px;
  }
</style>
</head>
<body>
<div class="canvas">
  <p class="size-label">Size: 6m x 3m</p>

  <section class="billboard">
    <svg class="contact-band" viewBox="0 0 822 412" aria-hidden="true">
      <rect x="490" y="364" width="332" height="14" fill="var(--steel-grey)"/>
      <polygon points="0,320 550,320 484,391 0,391" fill="var(--brand-blue)"/>
    </svg>

    <h1 class="brand-name">
      <span class="line-main">Harbour</span>
      <span class="line-sub">Frameworks</span>
    </h1>

    <div class="divider"></div>
    <p class="tagline">We are residential<br>and commercial<br>builders.</p>

    <svg class="phone-icon" viewBox="0 0 42 42" aria-hidden="true">
      <path d="M9 3 C5 5 2 9 4 16 C7 26 15 34 25 38 C31 40 35 37 37 33 L30 26 C28 27 26 29 24 28 C19 25 16 22 13 17 C12 15 14 13 15 11 Z" fill="var(--white)"/>
      <path d="M24 12 A7 7 0 0 1 30 18" stroke="var(--white)" stroke-width="2.4" fill="none" stroke-linecap="round"/>
      <path d="M25 6 A12 12 0 0 1 36 17" stroke="var(--white)" stroke-width="2.4" fill="none" stroke-linecap="round"/>
    </svg>
    <p class="phone-number">022 583 7092</p>
  </section>
</div>
</body>
</html>
```